Lantern Vale Photography business card design required

Needing business card made up for my new photography business.

Target Market(s)

Target will mostly be regular people with the occasional industrial or commercial customer.

Industry/Entity Type

Business

Font styles to use
Sans Serif

Colors

Designer to choose colors to be used in the design.

Requirements
Must have
• Morgan Tillbrook
Ph: 0437 262 508
Email: info@lanternvalephoto.example
Web: www.lanternvalephoto.example

On the back possibly links for social media including Facebook, Flickr and Instagram (links to be determined).

```html
<!DOCTYPE html>
<html lang="en">
<head>
<meta charset="utf-8">
<title>Lantern Vale Photography – Business Card</title>
<link rel="stylesheet" href="https://fonts.googleapis.com/css2?family=Cinzel:wght@400;700&display=swap">
<style>
  :root {
    --backdrop: #e8e8e8;
    --paper: #ffffff;
    --brand-blue: #05a3d1;
    --ring-grey: #4a4a4a;
    --ink: #2b2b2b;
  }
  html, body {
    margin: 0;
    padding: 0;
    width: 1200px;
    height: 720px;
    overflow: hidden;
    background: var(--backdrop);
  }
  .stage {
    position: relative;
    width: 1200px;
    height: 720px;
  }
  .card {
    position: absolute;
    top: 242px;
    width: 420px;
    height: 240px;
    background: var(--paper);
    box-shadow: 0 6px 18px rgba(0, 0, 0, 0.18);
  }
  .card--front { left: 147px; }
  .card--back  { left: 633px; }
  .card svg { display: block; width: 420px; height: 240px; }
  .card text { font-family: 'Cinzel', serif; }
  .band { fill: var(--brand-blue); }
  .paper { fill: var(--paper); }
  .hairline { fill: none; stroke: var(--paper); stroke-width: 2; }
  .lens-ring { fill: none; stroke: var(--ring-grey); stroke-width: 36; }
  .brand-name { fill: var(--ink); font-weight: 700; font-size: 18px; letter-spacing: 0.5px; }
  .contact-label { fill: var(--ink); font-size: 15px; font-weight: 400; }
  .social-tile { fill: var(--brand-blue); }
  .person-name { fill: var(--brand-blue); font-weight: 700; font-size: 14.5px; }
  .person-role { fill: var(--ink); font-size: 10.5px; font-weight: 700; }
  .contact-line { fill: var(--ink); font-size: 11px; font-weight: 700; }
  .icon { fill: none; stroke: var(--brand-blue); stroke-width: 1.4; }
  .icon-solid { fill: var(--brand-blue); }
</style>
</head>
<body>
<main class="stage">

  <!-- Front: social contact side -->
  <section class="card card--front">
    <svg viewBox="0 0 525 300" aria-label="Front of business card">
      <defs>
        <clipPath id="front-clip"><rect width="525" height="300"/></clipPath>
      </defs>
      <g clip-path="url(#front-clip)">
        <rect class="band" x="351" y="0" width="174" height="300"/>
        <circle class="paper" cx="347" cy="150" r="137"/>
        <circle class="hairline" cx="347" cy="150" r="153"/>
      </g>
      <circle class="lens-ring" cx="347" cy="150" r="95"/>

      <g class="social-links">
        <rect class="social-tile" x="315" y="133" width="15" height="15" rx="2"/>
        <rect class="social-tile" x="337" y="133" width="15" height="15" rx="2"/>
        <rect class="social-tile" x="359" y="133" width="15" height="15" rx="2"/>
      </g>
      <text class="contact-label" x="343" y="170" text-anchor="middle">Contact Me</text>

      <g class="brand">
        <text class="brand-name" x="24" y="146">Lantern Vale</text>
        <text class="brand-name" x="24" y="168">Photography</text>
      </g>
    </svg>
  </section>

  <!-- Back: personal details side -->
  <section class="card card--back">
    <svg viewBox="0 0 525 300" aria-label="Back of business card">
      <defs>
        <clipPath id="back-clip"><rect width="525" height="300"/></clipPath>
      </defs>
      <g clip-path="url(#back-clip)">
        <rect class="band" x="0" y="0" width="175" height="300"/>
        <circle class="paper" cx="177" cy="150" r="137"/>
        <circle class="hairline" cx="177" cy="150" r="153"/>
      </g>
      <circle class="lens-ring" cx="177" cy="150" r="95"/>

      <text class="person-name" x="177" y="147" text-anchor="middle">Morgan Tillbrook</text>
      <text class="person-role" x="177" y="163" text-anchor="middle">Photographer</text>

      <g class="brand">
        <text class="brand-name" x="505" y="70" text-anchor="end">Lantern Vale</text>
        <text class="brand-name" x="505" y="92" text-anchor="end">Photography</text>
      </g>

      <g class="contact-details">
        <text class="contact-line" x="488" y="257" text-anchor="end">0437 262 508</text>
        <text class="contact-line" x="488" y="272" text-anchor="end">info@lanternvalephoto.example</text>
        <text class="contact-line" x="488" y="287" text-anchor="end">www.lanternvalephoto.example</text>

        <g class="icon-phone">
          <path class="icon-solid" d="M495 250 q6 -4 12 0 l-1 3 h-3 l-0.5 -1.5 h-3 l-0.5 1.5 h-3 z"/>
          <rect class="icon-solid" x="497" y="254" width="8" height="4" rx="1"/>
        </g>
        <g class="icon-mail">
          <rect class="icon" x="495" y="264" width="12" height="9"/>
          <path class="icon" d="M495 264 l6 5 l6 -5"/>
        </g>
        <g class="icon-web">
          <rect class="icon" x="495" y="278" width="12" height="8"/>
          <path class="icon" d="M501 286 v2 M498 289 h6"/>
        </g>
      </g>
    </svg>
  </section>

</main>
</body>
</html>
```